Pinecrest Renovations - Get the creative juices going!!

Pinecrest does not do the actual renovation work. The company provides high end project management of renovation (primarily residential - with an eye toward commercial) The renovation work could look very different between projects. This company manages the work of contractors, architects and interior designers (either subcontracted directly by Pinecrest or hired by the client and entrusted to Pinecrest to manage). Clients are high end in the economic scale and the card needs to have a high end feel to it.

The owner is female, but the audience will be heavily slanted male. It should not be a "feminine" or "masculine" looking card. If anything, slant more on the masculine side. Clean, simple, yet creative and artistically appealing. The card design should complement and in no way compete with the logo.

When people think of our company: trust, integrity, dynamic, limitless possibilities, transition, energy, creative. We plan to expand in the future to be international.

There will also be a contest running for stationary. Please check that section, as well.

***Black is 80-90 percent black. Not stark black

Tight timeline. Needs cards printed quickly!

Residential

```html
<!DOCTYPE html>
<html lang="en">
<head>
<meta charset="utf-8">
<title>Pinecrest Renovations – Business Card</title>
<link rel="stylesheet" href="https://fonts.googleapis.com/css2?family=Montserrat:wght@600&family=Questrial&display=swap">
<style>
  :root {
    --backdrop: #e4e4e2;
    --card-dark: #3b3c40;
    --card-light: #ffffff;
    --accent: #1fa597;
    --text-light: #f2f2f2;
    --text-muted: #9c9da1;
    --brand-ink: #3b3c40;
  }
  * { margin: 0; padding: 0; box-sizing: border-box; }
  html, body {
    width: 1200px; height: 613px; overflow: hidden;
    background: var(--backdrop);
  }
  .business-card {
    position: absolute; left: 180px; top: 66px;
    width: 840px; height: 480px;
    background: var(--card-dark);
    box-shadow: 0 6px 18px rgba(0,0,0,.18);
    font-family: "Questrial", sans-serif;
  }
  .brand-panel {
    position: absolute; left: 0; top: 0;
    width: 250px; height: 100%;
    background: var(--card-light);
  }
  .brand-panel::after {
    content: ""; position: absolute; right: -11px; top: 96px;
    border-top: 11px solid transparent;
    border-bottom: 11px solid transparent;
    border-left: 11px solid var(--card-light);
  }
  .brand-lockup {
    position: absolute; left: 208px; bottom: 44px;
    transform-origin: left bottom;
    transform: rotate(-90deg);
    display: flex; align-items: center; gap: 14px;
    white-space: nowrap;
  }
  .brand-name {
    font-size: 27px; letter-spacing: 1px; text-transform: uppercase;
    color: var(--brand-ink); line-height: 1;
  }
  .brand-mark {
    width: 22px; height: 22px; background: var(--accent);
  }
  .holder {
    position: absolute; left: 272px; top: 86px; line-height: 1.1;
  }
  .holder-name {
    font-family: "Montserrat", sans-serif; font-weight: 600;
    font-size: 22px; color: var(--text-light);
  }
  .holder-role {
    font-size: 18px; color: var(--text-muted); letter-spacing: .5px; margin-top: 2px;
  }
  .corner-square {
    position: absolute; right: 92px; top: 96px;
    width: 64px; height: 64px;
    border: 2px solid var(--text-light);
  }
  .contact-list {
    position: absolute; right: 44px; top: 288px;
    list-style: none;
  }
  .contact-item {
    display: flex; justify-content: flex-end; align-items: center; gap: 22px;
    height: 38px;
    font-size: 19px; letter-spacing: 1.2px; color: var(--text-light);
  }
  .contact-icon {
    width: 28px; height: 28px; background: var(--accent);
    display: flex; align-items: center; justify-content: center;
  }
  .contact-icon svg { width: 18px; height: 18px; fill: none; stroke: #fff; stroke-width: 1.8; }
</style>
</head>
<body>
  <article class="business-card">
    <div class="brand-panel">
      <div class="brand-lockup">
        <span class="brand-name">Pinecrest Renovations</span>
        <span class="brand-mark"></span>
      </div>
    </div>

    <div class="holder">
      <p class="holder-name">Your Name</p>
      <p class="holder-role">Designation</p>
    </div>

    <div class="corner-square"></div>

    <ul class="contact-list">
      <li class="contact-item">
        <span>555 014 2290</span>
        <span class="contact-icon"><svg viewBox="0 0 18 18"><rect x="5" y="2" width="8" height="14" rx="1"/><line x1="8" y1="13.5" x2="10" y2="13.5"/></svg></span>
      </li>
      <li class="contact-item">
        <span>www.pinecrestreno.com</span>
        <span class="contact-icon"><svg viewBox="0 0 18 18"><circle cx="9" cy="9" r="6.5"/><ellipse cx="9" cy="9" rx="2.8" ry="6.5"/><line x1="2.5" y1="9" x2="15.5" y2="9"/></svg></span>
      </li>
      <li class="contact-item">
        <span>help@pinecrestreno.com</span>
        <span class="contact-icon"><svg viewBox="0 0 18 18"><rect x="2.5" y="4.5" width="13" height="9"/><polyline points="2.5,4.5 9,10 15.5,4.5"/></svg></span>
      </li>
      <li class="contact-item">
        <span>72 W.Harlow Ave CA 90417</span>
        <span class="contact-icon"><svg viewBox="0 0 18 18"><path d="M9 16s-5-5.2-5-8.6a5 5 0 0 1 10 0C14 10.8 9 16 9 16z"/><circle cx="9" cy="7.4" r="1.8"/></svg></span>
      </li>
    </ul>
  </article>
</body>
</html>
```